redesign corporate website (software courses)

We need a complete redesign of the current website: http://q-o-r.biz/ (training: http://q-o-r.biz/pt-br/treinamento/web ); more clear, different color, navigation, header, footer, whatever (side note: site will be based on bootstrap and drupal). Most important pages:

http://q-o-r.biz/pt-br/treinamento (trainingoverviewpage)
http://q-o-r.biz/ (frontpage)
http://q-o-r.biz/pt-br/treinamento/web (trianingdetailpage)

The design should be valid for further content pages (like http://q-o-r.biz/pt-br/desenvolvimentodesoftware) and pages with forms (http://q-o-r.biz/pt-br/contact or http://q-o-r.biz/pt-br/training/web/register)

Logo attached in white and black and black with shadow.

Some other examples of training sites (just content examples - not as template for similar layout):

http://www.brivatutor.example/packages/4817/Website-Development-Professional-training.html?advid=31&gclid=XQa93pLmw42HGtrk5BsjEZWKpR
http://www.code-lehrhaus.example/
http://www.devalto.example/cursos/kestrel-framework-ii/
http://www.varnholt-academy.example/lp/php-development-training.aspx?gclid=MT3hwqUvb52DJYRR8Bpexk9B7B

Industry/Entity Type

Software

```html
<!DOCTYPE html>
<html lang="en">
<head>
<meta charset="utf-8">
<title>Qor Software Institute</title>
<link rel="stylesheet" href="https://fonts.googleapis.com/css2?family=Raleway:wght@400;500;600;700&family=Lato:ital,wght@1,400&display=swap">
<style>
:root{
  --orange:#f47a20;
  --orange-deep:#e8661a;
  --rust:#9e3a0c;
  --ink:#222;
  --text:#555;
  --muted:#8a8a8a;
  --line:#e3e3e3;
  --footer:#1c1c1c;
  --footer-bar:#3a3a3a;
  --white:#fff;
  --teal:#5b9fc9;
  --green:#5cb872;
  --yellow:#f0c63a;
}
*{box-sizing:border-box;margin:0;padding:0}
html,body{width:685px;height:1200px;overflow:hidden;background:var(--white)}
body{font-family:"Raleway",sans-serif;color:var(--text);position:relative}
.abs{position:absolute}

/* header */
.site-header{position:absolute;top:0;left:0;width:685px;height:48px;background:rgba(255,255,255,.96);z-index:2}
.brand{left:58px;top:16px;font-weight:700;font-size:15px;line-height:16px;color:var(--ink);white-space:nowrap}
.main-nav{left:261px;top:20px;display:flex;gap:15px;font-size:7.5px;font-weight:600;color:var(--ink)}
.main-nav .active{color:var(--orange)}
.search{left:450px;top:15px;width:98px;height:17px;background:var(--white);border:1px solid #eee}
.search svg{position:absolute;right:4px;top:4px}
.social{display:flex;gap:6px}
.social span{width:18px;height:18px;border-radius:50%;background:var(--ink)}
.social span:first-child{background:var(--orange)}
.site-header .social{left:562px;top:15px}

/* hero */
.hero{top:48px;left:0;width:685px;height:227px;background:linear-gradient(90deg,#7d8591 0%,#9aa2ae 45%,#c9c9cc 70%,#8c8f96 100%)}
.hero-title{left:58px;top:52px;font-size:27px;font-weight:600;color:var(--white)}
.hero-copy{left:58px;top:90px;width:292px;font-size:8.6px;line-height:10.5px;color:var(--white)}
.btn-ghost{left:58px;top:142px;width:86px;height:24px;border:1.5px solid var(--white);color:var(--white);font-size:9.5px;font-weight:600;display:flex;align-items:center;justify-content:center}
.slider-arrow{top:84px;width:24px;height:48px;background:rgba(60,60,60,.55)}
.slider-arrow.prev{left:0;border-radius:0 24px 24px 0}
.slider-arrow.next{right:0;border-radius:24px 0 0 24px}
.slider-arrow svg{position:absolute;top:18px}

/* services */
.section-title{font-size:19px;font-weight:700;color:var(--ink);text-align:center}
.divider{height:1px;background:var(--line)}
.divider-ring{width:8px;height:8px;border:1px solid var(--line);border-radius:50%;background:var(--white)}
.service{top:357px;width:140px;text-align:center}
.service-icon{width:38px;height:38px;border-radius:50%;margin:0 auto}
.service h3{margin-top:12px;font-size:8.6px;font-weight:600;color:var(--ink)}
.service p{margin:14px auto 0;width:128px;height:34px;font-size:6.2px;line-height:8.4px;color:var(--muted)}
.btn-outline{margin:15px auto 0;width:64px;height:20px;border:1.2px solid var(--orange);color:var(--orange);font-size:6.8px;font-weight:600;display:flex;align-items:center;justify-content:center}

/* about band */
.about{top:534px;left:0;width:685px;height:188px;background:var(--orange)}
.video{left:58px;top:38px;width:225px;height:113px;border-radius:3px;overflow:hidden}
.video-frame{width:225px;height:93px;background:linear-gradient(135deg,#b69c6e,#d9c7a0 55%,#c8b18a)}
.video-bar{height:20px;background:#111;position:relative}
.video-bar .track{position:absolute;left:57px;top:9px;width:98px;height:2px;background:#555}
.video-bar .track i{display:block;width:34px;height:2px;background:var(--white)}
.video-bar .time{position:absolute;left:162px;top:6px;font-size:5px;color:#ccc}
.about h2{left:308px;top:37px;font-size:11.5px;font-weight:700;color:var(--white)}
.about p{left:308px;width:308px;font-size:6.5px;line-height:10.8px;color:var(--white)}

/* events & testimonials */
.block-title{font-size:11.5px;font-weight:500;color:var(--ink)}
.event{left:52px;width:255px;height:44px;border-bottom:1px solid var(--line);display:flex}
.event-date{width:41px;text-align:center;font-weight:700;color:var(--ink);padding-top:6px}
.event-date b{display:block;font-size:7.5px}
.event-date strong{display:block;font-size:14px;line-height:14px}
.event-text{border-left:1px solid var(--line);padding:4px 0 0 5px;font-size:9.6px;line-height:15px;color:var(--ink);width:214px}
.testimonial{left:342px;top:783px;width:284px;height:147px;background:var(--rust);color:var(--white)}
.avatar{left:117px;top:9px;width:46px;height:46px;border-radius:50%;background:radial-gradient(circle,#cfcfcf,#9a9a9a)}
.quote-name{left:0;width:284px;top:58px;text-align:center;font-size:5.8px}
.quote{left:34px;top:71px;width:240px;font-family:"Lato",sans-serif;font-style:italic;font-size:8.5px;line-height:14.8px;white-space:nowrap}
.qmark{font-family:"Lato",sans-serif;font-size:17px;font-weight:700}
.dots{left:121px;top:127px;display:flex;gap:3px}
.dots span{width:6.5px;height:6.5px;border-radius:50%;background:var(--white)}
.dots span.off{background:#c46f4c}

/* footer */
.site-footer{top:971px;left:0;width:685px;height:205px;background:var(--footer);color:#cfcfcf}
.site-footer .brand{color:var(--white);top:38px}
.footer-about{left:58px;top:78px;width:140px;font-size:6.4px;line-height:10.8px}
.site-footer .social{left:58px;top:144px}
.site-footer .social span{background:#555}
.site-footer .social span:first-child{background:var(--orange)}
.footer-head{font-size:8.4px;font-weight:700;color:var(--white);padding-bottom:6px;border-bottom:1px solid #666;width:131px}
.news{left:255px;width:140px;font-size:6px;line-height:10px}
.news-date{left:255px;font-size:6px;color:var(--orange)}
.field{left:459px;width:149px;height:20px;background:var(--white);border-radius:2px;font-size:6.6px;color:#999;display:flex;align-items:center;padding-left:27px}
.field svg{position:absolute;left:9px;top:6px}
.field.area{height:40px;align-items:flex-start;padding-top:8px}
.field.area svg{top:9px}
.btn-send{left:550px;top:170px;width:57px;height:19px;background:var(--orange);color:var(--white);font-size:6.6px;font-weight:700;display:flex;align-items:center;justify-content:center}
.footer-bar{top:1176px;left:0;width:685px;height:24px;background:var(--footer-bar);color:#bbb;font-size:6.4px;display:flex;align-items:center;justify-content:center}
</style>
</head>
<body>

<header class="site-header">
  <div class="brand abs">Qor Software Institute</div>
  <nav class="main-nav abs"><span class="active">HOME</span><span>TRAINING</span><span>ABOUT</span><span>CONTACT</span></nav>
  <div class="search abs"><svg width="8" height="8" viewBox="0 0 8 8"><circle cx="3.3" cy="3.3" r="2.5" fill="none" stroke="#999" stroke-width="1"/><path d="M5.2 5.2L7.5 7.5" stroke="#999" stroke-width="1.2"/></svg></div>
  <div class="social abs"><span></span><span></span><span></span></div>
</header>

<section class="hero abs" role="img" aria-label="Photo of a smiling professional woman in an office with colleagues in the background">
  <div class="slider-arrow prev abs"><svg width="12" height="12" viewBox="0 0 12 12" style="left:5px"><path d="M8 1L3 6l5 5" stroke="#fff" stroke-width="1.5" fill="none"/></svg></div>
  <div class="slider-arrow next abs"><svg width="12" height="12" viewBox="0 0 12 12" style="left:8px"><path d="M4 1l5 5-5 5" stroke="#fff" stroke-width="1.5" fill="none"/></svg></div>
  <h1 class="hero-title abs">Grow Your Expertise</h1>
  <p class="hero-copy abs">Take your career to the next level! QOR training and certification courses can get you where you want to go. The journey to a satisfying career as a QOR practitioner, Certified Lead Appraiser or QOR Instructor begins here.</p>
  <a class="btn-ghost abs">Read more</a>
</section>

<section class="services">
  <h2 class="section-title abs" style="left:0;width:685px;top:300px">SERVICES</h2>
  <div class="divider abs" style="left:285px;top:332px;width:112px"></div>
  <div class="divider-ring abs" style="left:337px;top:328px"></div>

  <div class="service abs" style="left:49px"><div class="service-icon" style="background:var(--teal)"></div><h3>Training</h3><p>We are privileged for being positioned in a region with IT ancestry. Therefore, from short courses to offer specializations to make it more competitive with the labor</p><a class="btn-outline">Read more</a></div>
  <div class="service abs" style="left:199px"><div class="service-icon" style="background:var(--green)"></div><h3>Software Development</h3><p>We invest a lot in developing the quality and scalability combined with modern production tools. So the final product is more satisfactory and reliable.</p><a class="btn-outline">Read more</a></div>
  <div class="service abs" style="left:340px"><div class="service-icon" style="background:var(--yellow)"></div><h3>Consulting</h3><p>We work to improve the bond of the system with the processes of IT implementations always seeking leverage and minimize risks</p><a class="btn-outline">Read more</a></div>
  <div class="service abs" style="left:499px"><div class="service-icon" style="background:var(--orange-deep)"></div><h3>Course WEB</h3><p>Watch our calendar for more information on the course WEB, learn how the web environment works and how to get along across the labor market</p><a class="btn-outline">Read more</a></div>
</section>

<section class="about abs">
  <div class="video abs">
    <div class="video-frame" role="img" aria-label="Video still of a laptop on a wooden desk with a phone and notebooks"></div>
    <div class="video-bar">
      <svg class="abs" style="left:8px;top:5px" width="40" height="10" viewBox="0 0 40 10"><circle cx="5" cy="5" r="4" fill="none" stroke="#fff" stroke-width="1"/><path d="M4 3l3 2-3 2z" fill="#fff"/><path d="M16 4h2l2-2v6l-2-2h-2z" fill="#fff"/><path d="M23 4v3M25 4v3M27 4v3M29 4v3" stroke="#fff" stroke-width=".8"/></svg>
      <div class="track"><i></i></div>
      <span class="time">01:30 / 04:55</span>
      <svg class="abs" style="left:198px;top:6px" width="22" height="8" viewBox="0 0 22 8"><rect x="0.5" y="1.5" width="6" height="5" fill="none" stroke="#fff"/><circle cx="17" cy="4" r="2.5" fill="none" stroke="#fff" stroke-width="1.2"/></svg>
    </div>
  </div>
  <h2 class="abs">Get To Know Us a Little Better!</h2>
  <p class="abs" style="top:58px">Lorem ipsum dolor sit amet, consectetur adipiscing elit. Pellentesque eu erat lacus, vel congue mauris. Fusce velit justo, faucibus eu sagittis ac, gravida quis tortor. Suspendisse non urna mi, quis tincidunt eros. Nullam tellus turpis, fringilla sit amet congue ut, luctus a nulla. Donec sit amet sapien neque, id ullamcorper diam. Nulla facilisi. Pellentesque pellentesque arcu a elit congue lacinia.</p>
  <p class="abs" style="top:122px">Nullam tellus turpis, fringilla sit amet congue ut, luctus a nulla. Donec sit amet sapien neque, id ullamcorper diam. Nulla facilisi. Pellentesque pellentesque arcu a elit congue lacinia.</p>
</section>

<section class="events">
  <h2 class="block-title abs" style="left:52px;top:743px">UPCOMING EVENTS</h2>
  <div class="divider abs" style="left:52px;top:768px;width:255px"></div>
  <div class="divider-ring abs" style="left:105px;top:764px"></div>
  <div class="event abs" style="top:777px"><div class="event-date"><b>FEB</b><strong>08</strong></div><div class="event-text">Right here we've got something you gonna<br>love!</div></div>
  <div class="event abs" style="top:821px"><div class="event-date"><b>FEB</b><strong>09</strong></div><div class="event-text">Lorem ipsum dolor sit ame consectet urip-<br>sum dolor sit ame</div></div>
  <div class="event abs" style="top:865px"><div class="event-date"><b>FEB</b><strong>08</strong></div><div class="event-text">Right here we've got something you gonna<br>love!</div></div>
</section>

<section class="testimonials">
  <h2 class="block-title abs" style="left:339px;top:742px">WHAT OUR STUDENTS HAVE TO SAY</h2>
  <div class="divider abs" style="left:339px;top:767px;width:218px"></div>
  <div class="divider-ring abs" style="left:431px;top:763px"></div>
  <div class="testimonial abs">
    <div class="avatar abs" role="img" aria-label="Portrait of the student"></div>
    <div class="quote-name abs">Teodor Vallance</div>
    <span class="qmark abs" style="left:15px;top:50px">“</span>
    <p class="quote abs">At vero eos et accusamus et iusto odio dignissimos duci-<br>mus qui blanditiis praesentium voluptatum delenti<br>atque corrupti quos dolores ete</p>
    <span class="qmark abs" style="left:250px;top:98px">”</span>
    <div class="dots abs"><span></span><span class="off"></span><span></span><span></span></div>
  </div>
</section>

<footer class="site-footer abs">
  <div class="brand abs">Qor Software Institute</div>
  <p class="footer-about abs">We are privileged for being positioned in a region with IT ancestry. Therefore, from short courses to offer specializations to make it more competitive with the labor market and train more competent professionals</p>
  <div class="social abs"><span></span><span></span><span></span></div>

  <h3 class="footer-head abs" style="left:254px;top:27px">RECENT NEWS</h3>
  <span class="news-date abs" style="top:63px">15.10.2013</span>
  <p class="news abs" style="top:76px">Maecenas et nisl pellentesque, fermentum ante facilisis, aliquet ligula.</p>
  <span class="news-date abs" style="top:107px">9.10.2013</span>
  <p class="news abs" style="top:120px">Lorem ipsum dolor sit amet, consectetur adipiscing elit.</p>
  <span class="news-date abs" style="top:151px">9.10.2013</span>
  <p class="news abs" style="top:164px">Aliquam eu leo adipiscing, imperdiet arcunec, malesuada lorem.</p>

  <h3 class="footer-head abs" style="left:459px;top:27px;width:131px">GET IN TOUCH</h3>
  <div class="field abs" style="top:64px"><svg width="9" height="9" viewBox="0 0 9 9"><circle cx="4.5" cy="3" r="2" fill="none" stroke="#bbb"/><path d="M1 9c0-2.5 7-2.5 7 0" fill="none" stroke="#bbb"/></svg>Full name</div>
  <div class="field abs" style="top:91px"><svg width="9" height="8" viewBox="0 0 9 8"><rect x=".5" y=".5" width="8" height="6" fill="none" stroke="#bbb"/><path d="M.5 .5l4 3.5 4-3.5" fill="none" stroke="#bbb"/></svg>Email</div>
  <div class="field area abs" style="top:119px"><svg width="9" height="8" viewBox="0 0 9 8"><path d="M.5.5h8v5H3l-2 2v-2H.5z" fill="none" stroke="#bbb"/></svg>Comments</div>
  <a class="btn-send abs">SEND</a>
</footer>
<div class="footer-bar abs">©2014 Qor Software Institute</div>

</body>
</html>
```